Health IT Software needs brochure design

We need a brochure for our health software startup that will most likely be used as an email attachment for our prospective clients (hospitals). However, it also needs to fit a printed version appropriately. Attached is a description of the project and guidance on the content that I feel would be helpful to use. Our one-page flyer is also attached.
Please use a standard letter size- 8.5 x 11 inches.
Looking for a 4 page design.

Colors
33b8a4
0455a3
ffffff
cee9f5

```html
<!DOCTYPE html>
<html lang="en">
<head>
<meta charset="utf-8">
<title>Meridia Brochure</title>
<link href="https://fonts.googleapis.com/css2?family=Montserrat:wght@500;600;700&family=Open+Sans:wght@400;600&display=swap" rel="stylesheet">
<style>
  :root {
    --navy: #0b3a73;
    --blue: #0455a3;
    --teal: #33b8a4;
    --ice: #cee9f5;
    --white: #ffffff;
    --grey: #c9ced6;
    --ink: #3c4654;
    --stage: #e6e7e9;
  }
  * { margin: 0; padding: 0; box-sizing: border-box; }
  html, body { width: 900px; height: 1200px; overflow: hidden; }
  body { background: var(--stage); font-family: "Open Sans", Arial, sans-serif; color: var(--ink); position: relative; }
  .page { position: absolute; width: 400px; height: 518px; background: var(--white); overflow: hidden; box-shadow: 0 2px 8px rgba(0,0,0,.12); }
  .page--cover { left: 33px; top: 55px; }
  .page--features { left: 467px; top: 55px; }
  .page--story { left: 33px; top: 628px; }
  .page--back { left: 467px; top: 628px; }
  .abs { position: absolute; }
  .brand { display: flex; align-items: center; gap: 6px; font-family: "Montserrat", Arial, sans-serif; font-weight: 600; color: var(--navy); }
  .brand__mark { width: 14px; height: 14px; background: var(--blue); }
  .photo { background: linear-gradient(135deg, var(--ice), #8fb3cf); }
  .body-text { font-size: 5.4px; line-height: 1.55; color: var(--ink); text-align: justify; }
  .section-head { display: flex; align-items: center; gap: 6px; font-family: "Montserrat", Arial, sans-serif; font-weight: 600; font-size: 9px; color: var(--navy); }
  .icon-dot { width: 15px; height: 15px; border-radius: 50%; background: var(--navy); display: flex; align-items: center; justify-content: center; }
  .sub-head { display: flex; align-items: center; gap: 4px; font-family: "Montserrat", Arial, sans-serif; font-weight: 600; font-size: 6.5px; color: var(--navy); }
  .sub-head .icon-dot { width: 9px; height: 9px; }
  .footer-band { position: absolute; left: 0; bottom: 0; width: 400px; height: 22px; }
  /* cover */
  .cover__title { left: 0; top: 300px; width: 400px; height: 40px; background: var(--navy); color: var(--white); font-family: "Montserrat", Arial, sans-serif; font-weight: 600; font-size: 11px; line-height: 1.3; text-align: center; padding-top: 7px; text-transform: uppercase; }
  .cover__note { left: 0; top: 348px; width: 400px; text-align: center; font-size: 5.2px; color: var(--ink); }
  .cover__url { left: 0; top: 412px; width: 400px; text-align: center; font-family: "Montserrat", Arial, sans-serif; font-weight: 700; font-size: 10px; color: var(--navy); }
  /* story */
  .story-tab { left: 22px; top: 118px; width: 60px; height: 16px; background: var(--navy); color: var(--white); font-family: "Montserrat", Arial, sans-serif; font-weight: 600; font-size: 7.5px; line-height: 16px; padding-left: 6px; }
  .story-rule { left: 22px; top: 134px; width: 356px; height: 1.5px; background: var(--navy); }
  /* back */
  .back__field { left: 0; top: 0; width: 400px; height: 418px; background: linear-gradient(160deg, #0d4d93 0%, var(--navy) 55%, #062a57 100%); }
  .contact { right: 24px; top: 462px; font-size: 5.4px; line-height: 1.9; color: var(--ink); }
  .contact__row { display: flex; align-items: center; gap: 4px; }
  .contact__row b { font-family: "Montserrat", Arial, sans-serif; color: var(--navy); font-weight: 600; }
  .contact__icon { width: 7px; height: 7px; border-radius: 50%; background: var(--navy); }
</style>
</head>
<body>

<!-- Page 1: Cover -->
<section class="page page--cover">
  <div class="abs brand" style="left:0;top:34px;width:400px;justify-content:center;font-size:17px;">
    <span class="brand__mark"></span><span>Meridia</span>
  </div>
  <svg class="abs" style="left:110px;top:80px" width="180" height="205" viewBox="0 0 180 205" role="img" aria-label="Photo of a medical team stacking hands together, framed in a hexagon">
    <defs>
      <linearGradient id="heroFill" x1="0" y1="0" x2="1" y2="1">
        <stop offset="0" stop-color="#cee9f5"/><stop offset="1" stop-color="#6f93b8"/>
      </linearGradient>
    </defs>
    <polygon points="90,2 178,52 178,153 90,203 2,153 2,52" fill="var(--navy)"/>
    <polygon points="90,9 171,56 171,149 90,196 9,149 9,56" fill="url(#heroFill)"/>
  </svg>
  <div class="abs cover__title">An EHR developed by physicians<br>and healthcare professionals</div>
  <div class="abs cover__note">With founders in practice across internal and family medicine</div>
  <div class="abs cover__url">www.meridiasoftware.com</div>
  <svg class="footer-band" style="height:40px" viewBox="0 0 400 40" preserveAspectRatio="none">
    <polygon points="0,16 250,16 240,40 0,40" fill="var(--navy)"/>
    <polygon points="256,16 400,6 400,40 246,40" fill="var(--grey)"/>
    <polygon points="0,10 260,10 257,14 0,14" fill="var(--grey)"/>
  </svg>
</section>

<!-- Page 2: Features -->
<section class="page page--features">
  <div class="abs section-head" style="left:120px;top:22px">
    <span class="icon-dot"><svg width="8" height="8" viewBox="0 0 8 8"><rect x="1.5" y="1" width="5" height="6" fill="none" stroke="#fff" stroke-width="1"/></svg></span>
    Organic Documentation
  </div>
  <div class="abs photo" style="left:22px;top:50px;width:86px;height:62px" role="img" aria-label="Laptop showing the charting screen"></div>
  <p class="abs body-text" style="left:150px;top:48px;width:228px">Clinicians chart in their own words while the system turns each note into structured data, so records stay natural, complete and ready for billing, reporting and care review without extra clicks or duplicate entry across every visit.<br>Templates adapt to each specialty and learn from daily use.</p>

  <div class="abs section-head" style="left:22px;top:160px">
    <span class="icon-dot"><svg width="8" height="8" viewBox="0 0 8 8"><circle cx="4" cy="3" r="1.6" fill="#fff"/><path d="M1 7.5 Q4 4 7 7.5" fill="#fff"/></svg></span>
    Patient Engagement
  </div>
  <p class="abs body-text" style="left:22px;top:186px;width:220px">Patients view results, message their care team and complete forms before arrival, which shortens visits and keeps every person informed and involved in decisions about their own health.</p>
  <div class="abs photo" style="left:290px;top:178px;width:88px;height:62px" role="img" aria-label="Laptop showing the patient portal"></div>

  <div class="abs section-head" style="left:22px;top:292px">
    <span class="icon-dot"><svg width="8" height="8" viewBox="0 0 8 8"><path d="M1.5 4 L3.3 6 L6.5 2" fill="none" stroke="#fff" stroke-width="1.1"/></svg></span>
    Risk Management/Quality Improvement
  </div>
  <p class="abs body-text" style="left:22px;top:318px;width:356px">Built-in alerts flag gaps in care, missing signatures and quality measures early, helping teams lower risk, meet reporting rules and improve outcomes across the hospital.</p>
  <div class="abs photo" style="left:290px;top:350px;width:88px;height:62px" role="img" aria-label="Laptop showing the quality dashboard"></div>

  <svg class="footer-band" viewBox="0 0 400 22" preserveAspectRatio="none">
    <polygon points="0,8 290,8 282,22 0,22" fill="var(--navy)"/>
    <polygon points="296,8 400,8 400,22 288,22" fill="var(--grey)"/>
  </svg>
</section>

<!-- Page 3: Security and Story -->
<section class="page page--story">
  <div class="abs section-head" style="left:22px;top:24px">
    <span class="icon-dot"><svg width="8" height="8" viewBox="0 0 8 8"><rect x="1.8" y="3.6" width="4.4" height="3.4" fill="#fff"/><path d="M2.7 3.6 V2.5 a1.3 1.3 0 0 1 2.6 0 V3.6" fill="none" stroke="#fff" stroke-width=".8"/></svg></span>
    Security
  </div>
  <p class="abs body-text" style="left:22px;top:48px;width:356px">All data is encrypted at rest and in transit, access is logged by role, and servers are hosted in audited facilities that meet current privacy standards for health records.</p>

  <div class="abs story-tab">Our Story</div>
  <div class="abs story-rule"></div>

  <div class="abs sub-head" style="left:22px;top:152px"><span class="icon-dot"></span>The Present</div>
  <p class="abs body-text" style="left:22px;top:168px;width:200px">Our team of physicians built this record after years of frustration with slow, rigid systems. Today it supports clinics and hospitals that want faster charting and clearer data.</p>
  <div class="abs photo" style="left:268px;top:150px;width:110px;height:104px;background:linear-gradient(135deg,#f3f1ee,#c9b59a)" role="img" aria-label="Wooden blocks showing a year on a desk"></div>

  <div class="abs photo" style="left:22px;top:290px;width:110px;height:84px;background:linear-gradient(135deg,#f1ece4,#bfa47f)" role="img" aria-label="Stacked wooden blocks forming steps"></div>
  <div class="abs sub-head" style="left:150px;top:292px"><span class="icon-dot"></span>The Future</div>
  <p class="abs body-text" style="left:150px;top:308px;width:228px">We are expanding analytics, mobile access and connections to labs and pharmacies, always guided by the people who use the software every day.</p>

  <svg class="footer-band" viewBox="0 0 400 22" preserveAspectRatio="none">
    <polygon points="0,8 290,8 282,22 0,22" fill="var(--navy)"/>
    <polygon points="296,8 400,8 400,22 288,22" fill="var(--grey)"/>
  </svg>
</section>

<!-- Page 4: Back cover -->
<section class="page page--back">
  <div class="abs back__field" role="img" aria-label="Deep blue background with a faint connected network pattern"></div>
  <svg class="abs" style="left:0;top:408px" width="400" height="20" viewBox="0 0 400 20" preserveAspectRatio="none">
    <polygon points="0,10 400,0 400,20 0,20" fill="var(--white)"/>
  </svg>
  <div class="abs brand" style="left:24px;top:470px;font-size:11px;">
    <span class="brand__mark" style="width:10px;height:10px"></span><span>Meridia</span>
  </div>
  <div class="abs contact">
    <div class="contact__row"><span class="contact__icon"></span><b>Call us today:</b>&nbsp;555-010-2453</div>
    <div class="contact__row"><span class="contact__icon"></span>www.meridiasoftware.com</div>
    <div class="contact__row"><span class="contact__icon"></span>info@meridiasoftware.com</div>
  </div>
</section>

</body>
</html>
```